Flat Belly Design Graphics for Social

I want to create 9 social media graphics (new Instagram size 4:5 (1080 x 1350 pixels) focusing on our Flat Belly Graphics, using the pics attached. Use the attached pics, NO RANDOM STOCK PHOTOGRAPHY. For the color scheme of the graphics, the color palette is attached. YOU MUST POST ALL 9 GRAPHICS IN ONE ENTRY.
Using the 3 titles below, create one set of graphics. 1) with all text, then for the others, use the pictures as detailed below in IMPORTANT:
1. 21-Night Lean Middle Reboot Beyond 50
2. The 20-Second Trim-Core Menu Guide
3. Starlet Tricks to a Slender Midline Beyond 50 - Zero Scalpel Needed
IMPORTANT:
Only use RK Pic 1 and RK Pic 2 with the title, 21-Night Lean Middle Reboot Beyond 50
Only use meal plan1 and meal plan2 pics with the title, 20-Second Trim-Core Menu Guide
Only use starlet tricks 1 and starlet tricks 2 pics with the title, Starlet Tricks to a Slender Midline Beyond 50 - Zero Scalpel Needed
women over 40

```html
<!DOCTYPE html>
<html lang="en">
<head>
<meta charset="utf-8">
<title>Lean Middle Social Graphics Set</title>
<link href="https://fonts.googleapis.com/css2?family=Quicksand:wght@500;600&display=swap" rel="stylesheet">
<style>
:root{
  --pink:#e499ad;
  --blush:#fbeef0;
  --ink:#2e5b5c;
  --white:#ffffff;
  --frame:#111111;
  --food:linear-gradient(135deg,#6b4a34 0%,#b9563f 35%,#7f9a46 65%,#5a3d2a 100%);
  --portrait:linear-gradient(160deg,#b79a83 0%,#efe9e6 45%,#f7f3f1 60%,#3a2d28 100%);
  --duo:linear-gradient(150deg,#7ec9d9 0%,#e9c6b6 45%,#d9b7a4 60%,#7ec9d9 100%);
}
html,body{margin:0;padding:0;width:1200px;height:750px;overflow:hidden;background:var(--white);}
.stage{position:absolute;left:0;top:0;width:2420px;height:1512px;transform:scale(0.49587);transform-origin:0 0;font-family:"Quicksand",sans-serif;color:var(--ink);}
.card{position:absolute;border:3px solid var(--frame);background:var(--blush);box-sizing:border-box;overflow:hidden;}
.band{position:absolute;background:var(--pink);}
.photo{position:absolute;}
.photo.food{background:var(--food);}
.photo.portrait{background:var(--portrait);}
.photo.duo{background:var(--duo);}
.slant{clip-path:polygon(7% 0,100% 0,93% 100%,0 100%);}
.round{border-radius:50%;}
.ring-pink{border:8px solid var(--pink);box-sizing:border-box;}
.halo{position:absolute;border-radius:50%;background:var(--blush);}
.logo{position:absolute;width:80px;height:80px;border:2px solid var(--white);border-radius:50%;box-sizing:border-box;display:flex;align-items:center;justify-content:center;text-align:center;color:var(--white);font-size:15px;line-height:20px;transform:translate(-50%,-50%);}
.icon{position:absolute;width:62px;height:62px;transform:translate(-50%,-50%);}
.icon.big{width:82px;height:82px;}
.title{position:absolute;margin:0;text-align:center;font-size:24px;line-height:29px;font-weight:500;white-space:nowrap;}
.title.sm{font-size:21px;line-height:29px;}
.title.lg{font-size:27px;line-height:33px;}
.rule{position:absolute;height:2px;background:var(--pink);}
.badge{position:absolute;border-radius:50%;background:var(--pink);border:6px solid var(--blush);box-sizing:border-box;transform:translate(-50%,-50%);}
.headline{position:absolute;white-space:nowrap;font-weight:500;}
.tag{display:inline-block;background:var(--pink);padding:0 12px;transform:rotate(-2deg);}
.dot{display:inline-flex;align-items:center;justify-content:center;width:52px;height:52px;border-radius:50%;background:var(--pink);}
</style>
</head>
<body>
<svg width="0" height="0" style="position:absolute" aria-hidden="true">
  <symbol id="clock" viewBox="0 0 60 60"><circle cx="30" cy="30" r="28" fill="none" stroke="#fff" stroke-width="2"/><path d="M30 30V15M30 30H41" stroke="#fff" stroke-width="2" fill="none" stroke-linecap="round"/><circle cx="30" cy="30" r="2" fill="#fff"/></symbol>
  <symbol id="calendar" viewBox="0 0 60 60"><circle cx="30" cy="30" r="28" fill="none" stroke="#fff" stroke-width="2"/><rect x="16" y="18" width="28" height="26" rx="4" fill="none" stroke="#fff" stroke-width="2"/><path d="M16 24H44" stroke="#fff" stroke-width="4"/><text x="30" y="40" text-anchor="middle" font-family="Quicksand,sans-serif" font-size="13" fill="#fff">21</text></symbol>
  <symbol id="figure" viewBox="0 0 60 60"><circle cx="30" cy="30" r="28" fill="none" stroke="#fff" stroke-width="2"/><path d="M25 15C19 25 31 33 24 46M36 15C42 25 30 33 37 46" fill="none" stroke="#fff" stroke-width="2" stroke-linecap="round"/><circle cx="26" cy="19" r="2" fill="#fff"/></symbol>
</svg>

<main class="stage">

  <!-- Menu guide, stacked photos -->
  <section class="card" style="left:280px;top:158px;width:424px;height:530px;">
    <div class="band" style="left:0;top:25px;width:424px;height:174px;"></div>
    <div class="logo" style="left:58px;top:109px;">YOUR<br>LOGO<br>HERE</div>
    <div class="photo food slant" style="left:118px;top:25px;width:282px;height:174px;" role="img" aria-label="Healthy foods arranged around a menu notepad"></div>
    <p class="title lg" style="left:0;top:230px;width:418px;">The 20-Second<br>Trim-Core Menu Guide</p>
    <div class="band" style="left:0;top:334px;width:424px;height:173px;"></div>
    <div class="photo food slant" style="left:36px;top:334px;width:284px;height:173px;" role="img" aria-label="Fresh produce and fish around a blank menu card"></div>
    <svg class="icon big" style="left:362px;top:418px;"><use href="#clock"/></svg>
  </section>

  <!-- All titles with menu photo -->
  <section class="card" style="left:760px;top:158px;width:425px;height:530px;">
    <div class="band" style="left:0;top:25px;width:425px;height:174px;"></div>
    <div class="logo" style="left:62px;top:109px;">YOUR<br>LOGO<br>HERE</div>
    <div class="photo food slant" style="left:112px;top:25px;width:290px;height:174px;" role="img" aria-label="Healthy foods arranged around a menu notepad"></div>
    <div class="band" style="left:0;top:222px;width:108px;height:285px;"></div>
    <svg class="icon" style="left:54px;top:270px;"><use href="#clock"/></svg>
    <svg class="icon" style="left:54px;top:362px;"><use href="#calendar"/></svg>
    <svg class="icon" style="left:54px;top:460px;"><use href="#figure"/></svg>
    <p class="title sm" style="left:115px;top:232px;width:300px;">The 20-Second<br>Trim-Core Menu Guide</p>
    <div class="rule" style="left:125px;top:308px;width:270px;"></div>
    <p class="title sm" style="left:115px;top:325px;width:300px;">21-Night Lean Middle<br>Reboot Beyond 50</p>
    <div class="rule" style="left:125px;top:400px;width:270px;"></div>
    <p class="title sm" style="left:115px;top:414px;width:300px;">Starlet Tricks to a<br>Slender Midline Beyond 50<br>Zero Scalpel Needed</p>
  </section>

  <!-- All titles with portrait -->
  <section class="card" style="left:1238px;top:158px;width:425px;height:530px;">
    <div class="band" style="left:0;top:25px;width:425px;height:174px;"></div>
    <div class="halo" style="left:41px;top:2px;width:220px;height:220px;background:var(--white);"></div>
    <div class="photo portrait round" style="left:51px;top:12px;width:200px;height:200px;" role="img" aria-label="Smiling woman in a white cropped sweater"></div>
    <div class="logo" style="left:331px;top:109px;">YOUR<br>LOGO<br>HERE</div>
    <div class="band" style="left:320px;top:222px;width:105px;height:285px;"></div>
    <svg class="icon" style="left:371px;top:270px;"><use href="#calendar"/></svg>
    <svg class="icon" style="left:371px;top:360px;"><use href="#clock"/></svg>
    <svg class="icon" style="left:371px;top:460px;"><use href="#figure"/></svg>
    <p class="title sm" style="left:10px;top:236px;width:300px;">21-Night Lean Middle<br>Reboot Beyond 50</p>
    <div class="rule" style="left:25px;top:308px;width:270px;"></div>
    <p class="title sm" style="left:10px;top:325px;width:300px;">The 20-Second<br>Trim-Core Menu Guide</p>
    <div class="rule" style="left:25px;top:400px;width:270px;"></div>
    <p class="title sm" style="left:10px;top:414px;width:300px;">Starlet Tricks to a<br>Slender Midline Beyond 50<br>Zero Scalpel Needed</p>
  </section>

  <!-- Reboot, single portrait -->
  <section class="card" style="left:1719px;top:158px;width:425px;height:530px;">
    <div class="band" style="left:127px;top:0;width:171px;height:190px;"></div>
    <div class="logo" style="left:210px;top:82px;">YOUR<br>LOGO<br>HERE</div>
    <div class="halo" style="left:72px;top:147px;width:280px;height:280px;background:var(--white);"></div>
    <div class="photo portrait round" style="left:86px;top:161px;width:252px;height:252px;" role="img" aria-label="Smiling woman in a white cropped sweater"></div>
    <div class="badge" style="left:175px;top:398px;width:84px;height:84px;"></div>
    <svg class="icon" style="left:175px;top:398px;"><use href="#calendar"/></svg>
    <p class="title" style="left:0;top:443px;width:419px;">21-Night Lean Middle<br>Reboot Beyond 50</p>
  </section>

  <!-- Starlet tricks, stacked photos -->
  <section class="card" style="left:67px;top:797px;width:434px;height:538px;">
    <div class="band" style="left:0;top:28px;width:434px;height:172px;"></div>
    <div class="logo" style="left:62px;top:112px;">YOUR<br>LOGO<br>HERE</div>
    <div class="photo portrait slant" style="left:130px;top:28px;width:275px;height:172px;background:linear-gradient(150deg,#f4efec,#c79b83 45%,#3b2c27 70%,#f1ece9);" role="img" aria-label="Two friends sharing a whispered secret"></div>
    <p class="title" style="left:0;top:236px;width:428px;font-size:23px;line-height:31px;">Starlet Tricks to a Slender Midline<br>Beyond 50 - Zero Scalpel Needed</p>
    <div class="band" style="left:0;top:336px;width:434px;height:174px;"></div>
    <div class="photo duo slant" style="left:30px;top:336px;width:280px;height:174px;" role="img" aria-label="Two friends whispering against a blue backdrop"></div>
    <svg class="icon big" style="left:366px;top:427px;"><use href="#figure"/></svg>
  </section>

  <!-- All titles with friends photo -->
  <section class="card" style="left:533px;top:797px;width:428px;height:538px;">
    <div class="band" style="left:0;top:28px;width:428px;height:172px;"></div>
    <div class="photo duo slant" style="left:36px;top:28px;width:280px;height:172px;" role="img" aria-label="Two friends whispering against a blue backdrop"></div>
    <div class="logo" style="left:364px;top:110px;">YOUR<br>LOGO<br>HERE</div>
    <div class="band" style="left:322px;top:228px;width:106px;height:284px;"></div>
    <svg class="icon" style="left:370px;top:281px;"><use href="#figure"/></svg>
    <svg class="icon" style="left:370px;top:380px;"><use href="#calendar"/></svg>
    <svg class="icon" style="left:370px;top:464px;"><use href="#clock"/></svg>
    <p class="title sm" style="left:8px;top:238px;width:305px;">Starlet Tricks to a<br>Slender Midline Beyond 50<br>Zero Scalpel Needed</p>
    <div class="rule" style="left:25px;top:339px;width:270px;"></div>
    <p class="title sm" style="left:8px;top:352px;width:305px;">The 20-Second<br>Trim-Core Menu Guide</p>
    <div class="rule" style="left:25px;top:425px;width:270px;"></div>
    <p class="title sm" style="left:8px;top:438px;width:305px;">21-Night Lean Middle<br>Reboot Beyond 50</p>
  </section>

  <!-- Menu guide collage -->
  <section class="card" style="left:996px;top:797px;width:431px;height:538px;">
    <div class="band" style="left:0;top:0;width:135px;height:538px;"></div>
    <div class="logo" style="left:71px;top:85px;">YOUR<br>LOGO<br>HERE</div>
    <div class="headline" style="left:183px;top:18px;font-size:28px;">The</div>
    <div class="headline" style="left:182px;top:55px;font-size:36px;"><span class="tag">20-Second</span></div>
    <div class="headline" style="right:70px;top:115px;font-size:28px;">Trim-Core</div>
    <div class="headline" style="right:24px;top:150px;font-size:28px;">Menu Guide</div>
    <div class="halo" style="left:15px;top:147px;width:250px;height:250px;"></div>
    <div class="photo food round ring-pink" style="left:32px;top:164px;width:216px;height:216px;" role="img" aria-label="Healthy foods arranged around a menu notepad"></div>
    <div class="photo portrait round ring-pink" style="left:252px;top:221px;width:152px;height:152px;" role="img" aria-label="Smiling woman in a white cropped sweater"></div>
    <div class="photo duo round ring-pink" style="left:154px;top:367px;width:152px;height:152px;" role="img" aria-label="Two friends whispering against a blue backdrop"></div>
  </section>

  <!-- Reboot collage -->
  <section class="card" style="left:1462px;top:797px;width:428px;height:538px;">
    <div class="band" style="left:0;top:0;width:130px;height:538px;"></div>
    <div class="logo" style="left:68px;top:85px;">YOUR<br>LOGO<br>HERE</div>
    <div class="headline" style="left:183px;top:32px;font-size:34px;"><span class="tag">21-Night</span></div>
    <div class="headline" style="right:24px;top:94px;font-size:26px;">Lean Middle Reboot</div>
    <div class="headline" style="right:24px;top:132px;font-size:28px;display:flex;align-items:center;gap:8px;">Beyond <span class="dot">50</span></div>
    <div class="halo" style="left:12px;top:147px;width:250px;height:250px;"></div>
    <div class="photo portrait round ring-pink" style="left:29px;top:164px;width:216px;height:216px;" role="img" aria-label="Smiling woman in a white cropped sweater"></div>
    <div class="photo duo round ring-pink" style="left:251px;top:221px;width:152px;height:152px;" role="img" aria-label="Two friends whispering against a blue backdrop"></div>
    <div class="photo food round ring-pink" style="left:149px;top:369px;width:152px;height:152px;" role="img" aria-label="Healthy foods arranged around a menu notepad"></div>
  </section>

  <!-- Starlet tricks collage -->
  <section class="card" style="left:1922px;top:797px;width:428px;height:538px;">
    <div class="band" style="left:0;top:0;width:130px;height:538px;"></div>
    <div class="logo" style="left:64px;top:85px;">YOUR<br>LOGO<br>HERE</div>
    <div class="headline" style="left:160px;top:40px;font-size:24px;">Starlet</div>
    <div class="headline" style="left:252px;top:24px;font-size:32px;"><span class="tag">Tricks</span></div>
    <div class="headline" style="right:18px;top:78px;font-size:18px;">to a Slender Midline Beyond 50</div>
    <div class="headline" style="right:22px;top:110px;font-size:19px;"><span class="tag" style="transform:none;padding:2px 14px;">Zero Scalpel Needed</span></div>
    <div class="halo" style="left:10px;top:147px;width:250px;height:250px;"></div>
    <div class="photo duo round ring-pink" style="left:27px;top:164px;width:216px;height:216px;" role="img" aria-label="Two friends whispering against a blue backdrop"></div>
    <div class="photo food round ring-pink" style="left:252px;top:222px;width:152px;height:152px;" role="img" aria-label="Healthy foods arranged around a menu notepad"></div>
    <div class="photo portrait round ring-pink" style="left:149px;top:369px;width:152px;height:152px;" role="img" aria-label="Smiling woman in a white cropped sweater"></div>
  </section>

</main>
</body>
</html>
```